MODERN DESIGN BUSINESS CARDS FOR A CREDIT REPAIR COMPANY

Our goal is to have a modern yet professional business card for our credit repair company. Something that'll catch the eye of our clients. PLEASE BE CREATIVE. WE WOULD LIKE TO SEE HOW THIS WOULD LOOK WITH A WHITE AND BLACK BACK GROUND.

Contact Information for Business Card

THIS WILL BE A DOUBLE SIDED BUSINESS CARD, THE COLORS WE WOULD LIKE TO HAVE IS BLACK, BLUES AND WHITE

Colors
3277b5
33a6d7
ffffff

Requirements
Must have
• MUST HAVE OUR LOGO, BUSINESS PHONE # (956 )482-7153, FACEBOOK LINK FACEBOOK.COM/VORMANTEKCREDITSOLUTIONS, CALL US FOR YOUR FREE CONSULTATION
Nice to have
• ITEMS WE DELETE: LATE PAYMENTS, CHARGE-OFFS, REPOSESSIONS, HOSPITAL BILLS, STUDENT LOANS, FORECLOSURES, CHILD SUPPORT AND BANKRUPTCIES.

```html
<!DOCTYPE html>
<html lang="en">
<head>
<meta charset="utf-8">
<title>Vormantek Credit Solutions – Business Card Back</title>
<link rel="stylesheet" href="https://fonts.googleapis.com/css2?family=Michroma&family=Montserrat:wght@500&display=swap">
<style>
  :root {
    --page: #ffffff;
    --card-light: #f7f7f7;
    --card-mid: #e4e4e4;
    --card-edge: #d6d6d6;
    --map-tone: #b9b9b9;
    --band: #2a2a2b;
    --band-ridge: #dcdcdc;
    --brand-blue: #2f5fb8;
    --text-light: #ffffff;
  }
  * { margin: 0; padding: 0; box-sizing: border-box; }
  html, body {
    width: 1200px;
    height: 800px;
    overflow: hidden;
    background: var(--page);
  }
  .card {
    position: relative;
    width: 1200px;
    height: 800px;
    border-radius: 52px;
    border: 2px solid var(--card-edge);
    overflow: hidden;
    background: radial-gradient(ellipse at 50% 40%, var(--card-light) 0%, var(--card-light) 40%, var(--card-mid) 100%);
  }
  .world-map {
    position: absolute;
    left: 170px;
    top: 100px;
    width: 860px;
    height: 490px;
    border-radius: 50%;
    background: radial-gradient(ellipse at 50% 50%, var(--map-tone) 0%, rgba(185,185,185,0.55) 45%, rgba(185,185,185,0) 72%);
    opacity: 0.6;
  }
  .brand {
    position: absolute;
    left: 275px;
    top: 270px;
    display: flex;
    align-items: center;
    gap: 40px;
  }
  .brand-dot {
    width: 150px;
    height: 150px;
    border-radius: 50%;
    background: var(--brand-blue);
    flex: none;
  }
  .brand-name {
    font-family: "Michroma", sans-serif;
    color: var(--brand-blue);
    font-weight: 400;
    line-height: 1;
  }
  .brand-name .name-main {
    display: block;
    font-size: 74px;
    letter-spacing: 2px;
  }
  .brand-name .name-sub {
    display: block;
    margin-top: 20px;
    font-size: 27px;
    letter-spacing: 6.5px;
  }
  .footer-band {
    position: absolute;
    left: 0;
    bottom: 0;
    width: 1200px;
    height: 200px;
  }
  .website {
    position: absolute;
    left: 0;
    width: 1200px;
    top: 652px;
    display: flex;
    justify-content: center;
    align-items: center;
    gap: 14px;
    font-family: "Montserrat", sans-serif;
    font-weight: 500;
    font-size: 32px;
    color: var(--text-light);
    letter-spacing: 0.5px;
  }
  .website svg { width: 46px; height: 46px; flex: none; }
</style>
</head>
<body>
  <div class="card">
    <div class="world-map" role="img" aria-label="Dotted world map in light grey"></div>

    <div class="brand">
      <div class="brand-dot"></div>
      <div class="brand-name">
        <span class="name-main">VORMANTEK</span>
        <span class="name-sub">CREDIT SOLUTIONS</span>
      </div>
    </div>

    <svg class="footer-band" viewBox="0 0 1200 200" preserveAspectRatio="none" aria-hidden="true">
      <path d="M0 132 L250 132 C300 132 310 22 380 12 L830 12 C900 22 900 132 960 132 L1200 132 L1200 200 L0 200 Z" fill="var(--band-ridge)"/>
      <path d="M0 138 L255 138 C305 138 318 30 385 20 L825 20 C892 30 895 138 955 138 L1200 138 L1200 200 L0 200 Z" fill="var(--band)"/>
    </svg>

    <div class="website">
      <svg viewBox="0 0 46 46" aria-hidden="true">
        <circle cx="23" cy="23" r="22" fill="var(--text-light)"/>
        <circle cx="23" cy="23" r="16" fill="none" stroke="var(--band)" stroke-width="2.5"/>
        <ellipse cx="23" cy="23" rx="7" ry="16" fill="none" stroke="var(--band)" stroke-width="2.5"/>
        <line x1="7" y1="23" x2="39" y2="23" stroke="var(--band)" stroke-width="2.5"/>
      </svg>
      <span>urwebsitename.com</span>
    </div>
  </div>
</body>
</html>
```